light box menu and wall graphics

HI My name is Derek Vantolla and I am putting together a Pebble Wagons franchise. We are a high quaulity coffee offering and the retail concept is for a in-line store in a busy shopping centre food court. We are a highly visible coffee offering with vibrant bright orange colour (pantone 021 / process m60_y100)
Orange might make a good background on the menu board as it needs to blend in with colour scheme. Also the text has to be at least 15ml and not too busy but clearly legible. The font is: Akzent Rounded
The twin light boxes being used is from http://www.brightframedepot.com.au/pg/lightboxes/new/sdb/light-box-2270K.aspx
They measure in total 3m wide X .6 height

There are two elements to this job, one is the twin menu boards and the other is the wall graphic.
please see wall graphic examples attached.
This graphic is to be painted onto the wall by a sign writter.
The design to go on the wall needs to be a synonymous with our quality coffee vison and match the shop design, I have examples of the type of wall art I am after attached. I was thinking somehow a Cart with wings would look neat and we could incorportate some text into it. Such as "coffee with character makes you feel good" and "Genuine Wagon" Flames could look amazing too!

My website is unfortunately down at the moment but I am attaching plenty

I have just added the menu in easy to read updated format.
Thanks to those who have expressed interest!
Updates

Hi Designers, I have just increased first prize by $100.00

Please note the signage boards run horizontally not vertically.  I have also added more artwork.

thanks

Derek

 HI there, thanks for joining.  I have just updated the brief to make it as clear as possible.

Hope you enjoy this experience.  I am here to answer any questions.

Derek

Thank you for accepting my invitation for this design job.

Look forward to seeing some designs as per brief.

Need to have this finished by Friday the 19th of October.  Thanks

Target Market(s)

Coffee lovers, kids who want hot chocolates, frappes,
etc

Industry/Entity Type

Shopping

Requirements
Must have
• Must have coffee in it for clarity.
Also in the menu any images of food or drink must be photo/posters attached

```html
<!DOCTYPE html>
<html lang="en">
<head>
<meta charset="utf-8">
<title>Pebble Wagons – Frappes &amp; Iced Drinks Light Box</title>
<link rel="stylesheet" href="https://fonts.googleapis.com/css2?family=Nunito:wght@800;900&family=Arimo:wght@400;700&display=swap">
<style>
  :root {
    --orange: #f7941d;
    --orange-deep: #e8892a;
    --ink: #231f20;
    --white: #ffffff;
    --grey-panel: #cfd0d0;
    --grey-panel-dark: #b9baba;
    --band: #141414;
    --url-orange: #f7941d;
  }
  * { margin: 0; padding: 0; box-sizing: border-box; }
  html, body { width: 1200px; height: 432px; overflow: hidden; }
  body { background: var(--orange); position: relative; font-family: "Nunito", sans-serif; }

  .board { position: absolute; inset: 0; }

  /* side posters */
  .poster { position: absolute; top: 0; width: 306px; height: 432px; overflow: hidden; }
  .poster--cup { left: 22px; background: linear-gradient(160deg, var(--grey-panel), var(--grey-panel-dark)); }
  .poster--frappe { left: 878px; width: 300px; background: var(--band); }

  .poster__footer { position: absolute; left: 0; right: 0; bottom: 0; height: 50px; background: var(--band); }
  .poster__founded { position: absolute; left: 20px; top: 6px; font-family: "Arimo", sans-serif; font-size: 4.5px; color: var(--white); letter-spacing: .2px; text-transform: uppercase; }
  .poster__url { position: absolute; left: 20px; top: 20px; font-family: "Arimo", sans-serif; font-weight: 700; font-size: 13.5px; color: var(--url-orange); }

  .brand-tile { position: absolute; width: 56px; height: 50px; background: var(--orange-deep); border: 1px solid #5a3a10; display: flex; align-items: center; justify-content: center; text-align: center; font-family: "Nunito", sans-serif; font-weight: 900; font-size: 10px; line-height: 1.05; color: var(--ink); }
  .poster--cup .brand-tile { left: 193px; top: 357px; }
  .poster--frappe .brand-tile { left: 194px; top: 357px; }

  .poster__headline { position: absolute; left: 0; right: 0; top: 20px; text-align: center; font-family: "Nunito", sans-serif; font-weight: 900; font-size: 22px; letter-spacing: .4px; line-height: 1.3; color: var(--ink); }
  .cup-photo { position: absolute; left: 105px; top: 95px; width: 104px; height: 180px; background: linear-gradient(180deg, #f4f2ec 0 5%, #b39268 5%, #a4835b 100%); border-radius: 2px 2px 8px 8px; }
  .poster__pitch { position: absolute; left: 0; right: 0; top: 294px; text-align: center; font-family: "Arimo", sans-serif; font-size: 9px; line-height: 1.3; color: var(--ink); }
  .poster__fine { position: absolute; left: 0; right: 0; top: 323px; text-align: center; font-family: "Arimo", sans-serif; font-size: 6.5px; line-height: 1.6; color: var(--ink); }

  .poster__tagline { position: absolute; left: 0; right: 0; top: 22px; text-align: center; font-family: "Arimo", sans-serif; font-size: 19px; color: var(--white); letter-spacing: .5px; }
  .frappe-photo { position: absolute; left: 0; top: 56px; width: 300px; height: 326px; background: radial-gradient(ellipse at 55% 18%, #6b4a3a 0 10%, #d9cfc7 32%, #c9bdb3 60%, #d8d3cd 100%); }

  /* menu */
  .menu { position: absolute; left: 328px; top: 0; width: 550px; height: 432px; color: var(--white); }
  .menu__section-head { position: absolute; left: 22px; right: 22px; display: flex; justify-content: space-between; align-items: baseline; color: var(--ink); }
  .menu__title { font-weight: 900; font-size: 38px; letter-spacing: .2px; line-height: 1.1; }
  .menu__price { font-weight: 900; font-size: 28px; letter-spacing: .6px; }
  .menu__price span { color: var(--white); }
  .menu__rule { position: absolute; height: 1.5px; background: var(--ink); }
  .menu__list { position: absolute; list-style: none; font-weight: 900; font-size: 22.5px; letter-spacing: .7px; line-height: 30.5px; white-space: nowrap; }
  .menu__list--wide { font-size: 23px; letter-spacing: .6px; line-height: 29px; }
</style>
</head>
<body>
<main class="board">

  <section class="poster poster--cup">
    <h2 class="poster__headline">You will look smarter<br>with this cup!</h2>
    <div class="cup-photo" role="img" aria-label="Photo of a kraft paper takeaway coffee cup with the café brand and LeafCup band"></div>
    <p class="poster__pitch">Lets face it being environmentally conscious<br>makes everyone look smarter!</p>
    <p class="poster__fine">Proudly serving Pebble Wagons coffee in our new plastic free,<br>compostable &amp; biodegradable Kraft paper LeafCup.</p>
    <footer class="poster__footer">
      <span class="poster__founded">Founded in 2004 Harbourton, North Queensland</span>
      <span class="poster__url">www.pebblewagons.com.au</span>
    </footer>
    <div class="brand-tile">Pebble<br>Wagons</div>
  </section>

  <section class="menu">
    <header class="menu__section-head" style="top:8px">
      <h1 class="menu__title">Frappes</h1>
      <p class="menu__price">M<span>$4.9</span> L<span>$5.5</span></p>
    </header>
    <div class="menu__rule" style="left:22px;width:506px;top:57px"></div>
    <ul class="menu__list" style="left:30px;top:70px">
      <li>Vanilla</li><li>Hazelnut</li><li>Caramel</li><li>Chocolate</li><li>Coffee</li><li>Chai</li>
    </ul>
    <ul class="menu__list" style="left:213px;top:70px">
      <li>Mango</li><li>Strawberry</li><li>Pineapple Paradise</li><li>+50C Banana Smoothie</li>
    </ul>
    <div class="menu__rule" style="left:27px;width:506px;top:269px;height:1px"></div>

    <header class="menu__section-head" style="top:280px">
      <h1 class="menu__title">Iced Drinks</h1>
      <p class="menu__price">M<span>$4.9</span> L<span>$5.5</span></p>
    </header>
    <ul class="menu__list menu__list--wide" style="left:22px;top:336px">
      <li>Iced Chocolate - served with ice cream</li>
      <li>Iced Coffee - served with ice cream</li>
    </ul>
  </section>

  <section class="poster poster--frappe">
    <p class="poster__tagline">coffee with character</p>
    <div class="frappe-photo" role="img" aria-label="Photo of a frappe in a tall glass topped with a chocolate swirl, with the word frappe in script"></div>
    <footer class="poster__footer">
      <span class="poster__founded">Founded in 2004 Harbourton, North Queensland</span>
      <span class="poster__url">www.pebblewagons.com.au</span>
    </footer>
    <div class="brand-tile">Pebble<br>Wagons</div>
  </section>

</main>
</body>
</html>
```